Business Cards & Stationary for Broadcast Company

We are a satellite company launching a new exciting brand by the name of "Veloran". Veloran is a broadcasting solution provider that gives end-to-end solutions to TV channels and other content providers to deliver and distribute their content globally. Weather it be TV channels that need to be broadcasted in their local regions or internationally, or its collection of news from various locations, or even coverage of special sports or other events, we provide the technology and services to make that happen.
we need a design for business cards as our top priority but also require letterhead and envelope design as well.
Business card will include the following information
Name: Karim Yusof
Designation: General Manager
Mobile (M): +92 321 4718296
+971 50 2846193 (UAE)
Direct (D): +92 213 4609142
Office (O): +92 213 4602518-22
Fax (F): +92 213 4609142
Email (E): karim@veloran.biz
Website: www.veloran.biz

```html
<!DOCTYPE html>
<html lang="en">
<head>
<meta charset="utf-8">
<title>Veloran Business Card</title>
<link href="https://fonts.googleapis.com/css2?family=Arimo:wght@400;700&display=swap" rel="stylesheet">
<style>
  :root {
    --backdrop: #e9eaec;
    --card: #ffffff;
    --brand-blue: #0767a8;
    --ink: #3a3a3c;
    --ink-soft: #4a4a4d;
    --mark-blue: #2fa8dd;
  }
  * { box-sizing: border-box; margin: 0; padding: 0; }
  html, body { width: 1200px; height: 1000px; overflow: hidden; }
  body {
    background: var(--backdrop);
    font-family: "Arimo", Arial, sans-serif;
    color: var(--ink);
    position: relative;
  }
  .card {
    position: absolute;
    width: 660px;
    height: 380px;
    background: var(--card);
    overflow: hidden;
    box-shadow: 0 6px 18px rgba(0,0,0,0.18);
  }
  .card--front { left: 110px; top: 100px; }
  .card--back { left: 435px; top: 520px; }

  .wordmark {
    position: absolute;
    display: flex;
    align-items: center;
    gap: 12px;
  }
  .wordmark__dot {
    border-radius: 50%;
    background: var(--mark-blue);
  }
  .wordmark__name { color: var(--ink); font-weight: 400; letter-spacing: 1px; }

  .card--front .wordmark { left: 0; right: 0; top: 120px; justify-content: center; }
  .card--front .wordmark__dot { width: 26px; height: 26px; }
  .card--front .wordmark__name { font-size: 40px; }

  .name-band {
    position: absolute;
    left: 0; right: 0; bottom: 0;
    height: 96px;
    background: var(--brand-blue);
    display: flex;
    align-items: center;
    justify-content: center;
  }
  .name-band__name { color: #fff; font-weight: 700; font-size: 24px; letter-spacing: 0.5px; }

  .card--back .wordmark { left: 40px; top: 70px; }
  .card--back .wordmark__dot { width: 20px; height: 20px; }
  .card--back .wordmark__name { font-size: 30px; }

  .holder { position: absolute; right: 40px; top: 178px; text-align: right; }
  .holder__name { font-size: 22px; font-weight: 700; letter-spacing: 3px; color: var(--ink); }
  .holder__title { font-size: 14px; color: var(--ink-soft); margin-top: 16px; }
  .divider {
    position: absolute;
    left: 18px; right: 10px; top: 212px;
    height: 3px;
    background: var(--brand-blue);
  }

  .contacts { position: absolute; font-size: 14px; color: var(--ink); line-height: 1.05; }
  .contact { position: absolute; display: flex; align-items: flex-start; gap: 6px; white-space: nowrap; }
  .contact__tag {
    display: inline-block;
    background: var(--brand-blue);
    color: #fff;
    font-size: 12px;
    padding: 2px 3px;
    line-height: 1.1;
    margin-top: 2px;
  }
  .contact__icon { width: 22px; height: 18px; flex: none; }
  .contact small { font-size: 11px; }
</style>
</head>
<body>

  <section class="card card--front" aria-label="Business card front">
    <div class="wordmark">
      <span class="wordmark__dot"></span>
      <span class="wordmark__name">VELORAN</span>
    </div>
    <div class="name-band">
      <span class="name-band__name">KARIM YUSOF</span>
    </div>
  </section>

  <section class="card card--back" aria-label="Business card back">
    <div class="wordmark">
      <span class="wordmark__dot"></span>
      <span class="wordmark__name">VELORAN</span>
    </div>

    <div class="holder">
      <div class="holder__name">Karim Yusof</div>
      <div class="holder__title">General Manager</div>
    </div>
    <div class="divider"></div>

    <div class="contacts">
      <div class="contact" style="left:60px; top:296px;">
        <span class="contact__tag">(M)</span>
        <span>+92 321 4718296<br>+971 50 2846193<small>(UAE)</small></span>
      </div>
      <div class="contact" style="left:62px; top:340px;">
        <svg class="contact__icon" viewBox="0 0 22 18" aria-label="Fax">
          <rect x="0" y="0" width="22" height="18" fill="#0767a8"/>
          <rect x="6" y="3" width="10" height="4" fill="#fff"/>
          <rect x="3" y="8" width="16" height="6" fill="#fff"/>
          <rect x="6" y="11" width="10" height="4" fill="#0767a8" stroke="#fff" stroke-width="1"/>
        </svg>
        <span style="margin-top:2px;">92 213 4609142</span>
      </div>

      <div class="contact" style="left:270px; top:283px;">
        <span class="contact__tag">(D)</span>
        <span style="margin-top:2px;">+92 213 4609142</span>
      </div>
      <div class="contact" style="left:272px; top:327px;">
        <span class="contact__tag">(O)</span>
        <span style="margin-top:2px;">+92 213 4602518-22</span>
      </div>

      <div class="contact" style="left:465px; top:268px;">
        <svg class="contact__icon" viewBox="0 0 22 18" aria-label="Email">
          <rect x="1" y="2" width="20" height="14" fill="#fff" stroke="#0767a8" stroke-width="2"/>
          <polyline points="1,2 11,10 21,2" fill="none" stroke="#0767a8" stroke-width="2"/>
        </svg>
        <span style="margin-top:2px;">karim@veloran.biz</span>
      </div>
      <div class="contact" style="left:465px; top:308px;">
        <svg class="contact__icon" viewBox="0 0 22 18" aria-label="Website">
          <rect x="0" y="0" width="22" height="18" fill="#0767a8"/>
          <circle cx="11" cy="9" r="6.5" fill="none" stroke="#fff" stroke-width="1.2"/>
          <ellipse cx="11" cy="9" rx="3" ry="6.5" fill="none" stroke="#fff" stroke-width="1"/>
          <line x1="4.5" y1="9" x2="17.5" y2="9" stroke="#fff" stroke-width="1"/>
        </svg>
        <span style="margin-top:2px;">www.veloran.biz</span>
      </div>
    </div>
  </section>

</body>
</html>
```